HANDYMAN SERVICES

we provide a good,and reliable service.we do all aspects of home improvement ,also all garden services,and any repairs,no job too small,free quotes .
I am aiming towards the general public for clients,also be doing special rates for the elderly,and reducing the price for anyone who does a friend reference. It will be free quotes/consultation,all work will be guaranteed.
Now the type of work we do is cctv installation,decking,patio/driveway cleaning,garages for erecting/repairs,house/garage clearances,fit alarm systems,fit or repair windows/doors,lay patios,repair roofs,decorate interior/external,erect ariaels,lay driveways,erect or repair fencing,lay drainage,repair or erect guttering and soffits,water features,erect or repair kitchens/bathrooms,also plastering,lay lawns or repair,also repair/erect sheds.
Home Improvement

```html
<!DOCTYPE html>
<html lang="en">
<head>
<meta charset="utf-8">
<title>Handyman Services – Home Improvement Flyer</title>
<link rel="stylesheet" href="https://fonts.googleapis.com/css2?family=Almendra+SC&family=Lobster+Two:ital,wght@1,700&family=Roboto+Condensed:wght@400;500&display=swap">
<style>
  :root {
    --backdrop: #b3070f;
    --ribbon: #b0101a;
    --gold: #ffe21a;
    --title-edge: #6b0a0a;
    --cream-light: #fffbe0;
    --cream: #fbf0b4;
    --ink: #141414;
    --navy: #0d2b5f;
    --white: #ffffff;
    --worker-top: #6a7c9c;
    --worker-bottom: #a88a5e;
    --roof-top: #c66a48;
    --roof-bottom: #a9502f;
    --installer-top: #eeeef0;
    --installer-bottom: #d9dce4;
  }
  * { box-sizing: border-box; margin: 0; padding: 0; }
  html, body {
    width: 1200px; height: 1006px; overflow: hidden;
    background: var(--backdrop);
  }
  .flyer {
    position: absolute; left: 73px; top: 68px;
    width: 1054px; height: 742px;
    background: linear-gradient(90deg, var(--cream-light) 30%, var(--cream) 100%);
    overflow: hidden;
    box-shadow: 0 8px 24px rgba(0,0,0,.35);
  }
  .photo { position: absolute; }
  .photo--worker {
    left: 0; top: 0; width: 355px; height: 742px;
    background: linear-gradient(180deg, var(--worker-top), var(--worker-bottom));
  }
  .photo--roof {
    left: 695px; top: 300px; width: 359px; height: 195px;
    background: linear-gradient(180deg, var(--roof-top), var(--roof-bottom));
  }
  .photo--installer {
    left: 695px; top: 495px; width: 359px; height: 247px;
    background: linear-gradient(180deg, var(--installer-top), var(--installer-bottom));
  }
  .ribbon {
    position: absolute; left: 362px; top: 32px;
    width: 692px; height: 66px;
  }
  .ribbon svg { position: absolute; inset: 0; }
  .ribbon__title {
    position: absolute; left: 30px; right: 0; top: 2px;
    font-family: "Almendra SC", serif;
    font-weight: 400;
    font-size: 56px; line-height: 62px;
    color: var(--gold);
    letter-spacing: 1px;
    text-align: center;
    -webkit-text-stroke: 1.5px var(--title-edge);
  }
  .tagline {
    position: absolute; left: 420px; width: 600px; top: 100px;
    font-family: "Lobster Two", cursive;
    font-style: italic; font-weight: 700;
    font-size: 35px; line-height: 44px;
    color: var(--ink); text-align: center;
  }
  .services {
    position: absolute; left: 355px; top: 300px;
    width: 340px; height: 442px;
    background: var(--navy);
  }
  .services__heading {
    position: absolute; left: 18px; top: 8px;
    font-family: "Lobster Two", cursive;
    font-style: italic; font-weight: 700;
    font-size: 26px; color: var(--gold);
  }
  .services__rule {
    position: absolute; left: 166px; right: 0; top: 32px;
    border-top: 2px dotted var(--gold);
  }
  .services__list {
    position: absolute; left: 0; right: 0; top: 46px;
    list-style: none; text-align: center;
    font-family: "Roboto Condensed", sans-serif;
    font-weight: 400; font-size: 16.5px; line-height: 27px;
    color: var(--white); text-transform: uppercase;
  }
</style>
</head>
<body>
  <main class="flyer">
    <div class="photo photo--worker" role="img" aria-label="Photo: handyman holding a cordless drill, wearing a leather tool belt"></div>

    <div class="ribbon">
      <svg width="692" height="66" viewBox="0 0 692 66" aria-hidden="true">
        <polygon points="0,0 692,0 692,66 0,66 22,33" fill="var(--ribbon)"/>
      </svg>
      <h1 class="ribbon__title">HANDYMAN SERVICES</h1>
    </div>

    <p class="tagline">providing good and reliable service.<br>We do all aspects of home<br>improvement, also all garden services,<br>and any repairs, no job too small.</p>

    <section class="services">
      <h2 class="services__heading">What We Do</h2>
      <div class="services__rule"></div>
      <ul class="services__list">
        <li>CCTV Installation | Decking |</li>
        <li>Patio/Driveway Cleaning |</li>
        <li>Garages for Erecting/Repairs |</li>
        <li>Fit Alarm Systems | Repair Roofs |</li>
        <li>House/Garage Clearances |</li>
        <li>Fit or Repair Windows/Doors |</li>
        <li>Decorate Interior/External |</li>
        <li>Erect Ariaels | Lay Driveways |</li>
        <li>Erect or Repair Fencing | Lay Patios |</li>
        <li>Lay Drainage | Water Features |</li>
        <li>Repair or Erect Guttering and Soffits |</li>
        <li>Lay Lawns or Repair | Also Plastering |</li>
        <li>Erect or Repair Kitchens/Bathrooms |</li>
        <li>Also Repair/Erect Sheds.</li>
      </ul>
    </section>

    <div class="photo photo--roof" role="img" aria-label="Photo: worker repairing a tiled roof"></div>
    <div class="photo photo--installer" role="img" aria-label="Photo: technician installing a security camera"></div>
  </main>
</body>
</html>
```